I need a great, modern, professional website for my paint contracting company, Brookhollow Paint Contractors, LLC. I have many good pix that can be used from jobs completed that would be attractive. We do commercial, residential and industrial jobs. I’m fully insured and licensed, including holding a General Contractor’s License as a Subcontractor. I know nothing about coding websites. I’ll have my assistant get on tomorrow and learn how to drop files. I’m not sure what files to send. This will be difficult at best, it being able to talk this through. Oh well. What’s next?

Target Market(s)

General Contractors

Industry/Entity Type

Paint Contracting

Coding

Coded - Design and coding required

Font styles to use
Sans Serif

Colors
00AB8E
00BBA5
67D7C9
C6EFE9
E9F9F6

Requirements
Must have
• Pix of completed jobs, bio, maybe testimonials from happy customers? ….
Nice to have
• I’d like it to have a modern appeal, but still have some warmth.
Should not have
• ??

```html
<!DOCTYPE html>
<html lang="en">
<head>
<meta charset="utf-8">
<title>Brookhollow Paint Contractors, LLC</title>
<link href="https://fonts.googleapis.com/css2?family=Poppins:ital,wght@0,400;0,500;0,600;0,700;1,400&display=swap" rel="stylesheet">
<style>
:root{
  --green:#00AB8E;
  --teal:#00BBA5;
  --mint:#67D7C9;
  --pale:#C6EFE9;
  --wash:#E9F9F6;
  --ink:#1b1b1b;
  --body:#444;
  --navy:#1d3c78;
  --red:#c0262d;
  --footer:#1d1d1d;
  --star:#f0811b;
}
*{box-sizing:border-box;margin:0;padding:0}
html,body{width:1200px;height:5115px;overflow:hidden}
body{font-family:'Poppins',sans-serif;color:var(--body);background:#fff;position:relative}
section,header,footer{position:absolute;left:0;width:1200px}
.abs{position:absolute}
.photo{position:absolute;display:block}
.btn{position:absolute;display:flex;align-items:center;justify-content:center;background:var(--green);color:#fff;font-size:14px;font-weight:600;text-transform:uppercase;letter-spacing:.3px}
.title{position:absolute;left:0;width:1200px;text-align:center;font-size:38px;font-weight:700;color:var(--ink);text-transform:uppercase}
.rule{position:absolute;height:3px;width:70px;left:565px}

/* header */
.site-header{top:0;height:100px;background:#fff}
.brand{position:absolute;left:100px;top:14px;color:var(--green);font-weight:700;font-size:25px;line-height:34px;text-transform:uppercase}
.contact-bar{position:absolute;top:12px;left:555px;display:flex;gap:26px;font-size:15px;color:var(--ink);font-weight:500;align-items:center}
.contact-bar span{display:flex;align-items:center;gap:8px}
.ico-circle{width:32px;height:32px;border:2px solid var(--green);border-radius:50%;display:flex;align-items:center;justify-content:center}
.main-nav{position:absolute;left:467px;top:60px;width:733px;height:40px;background:var(--green);display:flex;align-items:center;padding-left:38px;color:#fff;font-size:14px;font-weight:500}
.main-nav a{color:#fff;text-decoration:none}
.main-nav i{font-style:normal;margin:0 30px}

/* hero */
.hero{top:100px;height:630px}
.hero h1{position:absolute;left:100px;top:192px;font-size:46px;line-height:48px;font-weight:600;color:var(--ink);text-transform:uppercase}
.hero p{position:absolute;left:100px;top:302px;width:470px;font-size:14.5px;line-height:30px;color:var(--ink)}
.arrow{position:absolute;width:24px;height:40px}

/* about */
.about{top:730px;height:563px}
.about-frame{position:absolute;left:100px;top:75px;width:470px;height:402px;border-left:6px solid var(--green);border-top:6px solid var(--green)}
.about h2{position:absolute;left:651px;top:98px;font-size:38px;font-weight:700;color:var(--ink)}
.about p{position:absolute;left:651px;top:170px;width:455px;font-size:14px;line-height:32.5px;color:var(--ink)}

/* services */
.services{top:1293px;height:657px;background:linear-gradient(180deg,var(--teal),var(--green))}
.services .title{color:#fff;top:70px}
.card{position:absolute;top:158px;width:320px;height:415px;background:#fff;border-radius:4px;overflow:hidden;text-align:center}
.card .photo{left:0;top:0;width:320px;height:225px}
.card .badge{position:absolute;left:128px;top:185px;width:64px;height:64px;border-radius:50%;background:#fff;display:flex;align-items:center;justify-content:center}
.card h3{position:absolute;top:270px;left:0;width:100%;font-size:20px;font-weight:600;color:var(--ink)}
.card p{position:absolute;top:308px;left:10px;right:10px;font-size:14.5px;line-height:29px}
.card a{position:absolute;top:375px;left:0;width:100%;font-size:13.5px;font-weight:600;color:var(--green);text-decoration:underline}

/* gallery */
.gallery{top:1950px;height:991px}
.gallery .title{top:96px}

/* testimonials */
.reviews{top:2941px;height:626px;background:var(--wash)}
.reviews .title{top:72px}
.quote{position:absolute;top:205px;width:482px;height:232px;background:#fff;border-top:4px solid var(--navy);border-radius:14px 14px 4px 4px;text-align:center;box-shadow:0 4px 14px rgba(0,0,0,.06)}
.quote p{position:absolute;top:68px;left:30px;right:30px;font-size:15.5px;line-height:34px;font-style:italic;color:var(--ink)}
.quote .mark{position:absolute;right:14px;bottom:-28px;font-size:110px;line-height:1;color:#cfcfcf;font-weight:700}
.avatar{position:absolute;top:-34px;left:193px;width:96px;height:96px;border-radius:50%;background:linear-gradient(160deg,#d8d8d8,#9aa0a6);border:4px solid #fff}
.who{position:absolute;top:470px;width:482px;text-align:center;font-size:16px;color:var(--ink);font-weight:500}
.stars{position:absolute;top:496px;width:482px;text-align:center;color:var(--star);font-size:16px;letter-spacing:1px}
.dots{position:absolute;top:540px;left:540px;display:flex;gap:10px}
.dots i{display:block;width:34px;height:3px;background:#9bb3cf}
.dots i.on{background:var(--navy)}

/* blog */
.blog{top:3567px;height:641px}
.blog .title{top:83px}
.post{position:absolute;top:177px;width:314px;height:359px}
.post .photo{left:0;top:0;width:314px;height:190px}
.post .date{position:absolute;right:14px;top:12px;width:52px;height:52px;border-radius:50%;background:var(--green);color:#fff;font-size:12px;font-weight:600;line-height:14px;display:flex;flex-direction:column;align-items:center;justify-content:center}
.post .box{position:absolute;left:8px;right:8px;top:170px;height:189px;background:#fff;box-shadow:0 2px 10px rgba(0,0,0,.12);text-align:center;padding-top:14px}
.meta{font-size:11px;color:#666;display:flex;justify-content:center;gap:14px}
.meta span{display:flex;align-items:center;gap:4px}
.post h4{font-size:15.5px;line-height:23px;font-weight:600;color:var(--ink);margin-top:6px;text-transform:uppercase}
.post p{font-size:13px;line-height:29px;margin-top:4px;padding:0 10px;color:var(--ink)}

/* contact */
.get-in-touch{top:4208px;height:565px;overflow:hidden}
.get-in-touch h2{position:absolute;left:662px;top:84px;font-size:33px;font-weight:600;color:var(--ink);text-transform:uppercase}
.field{position:absolute;left:662px;width:437px;height:38px;background:#fff;border:1px solid #d3d3d3;font-size:13px;color:#333;padding:10px 14px}
.field.msg{height:92px}

/* footer */
.site-footer{top:4773px;height:342px;background:var(--footer);color:#ddd}
.foot-brand{position:absolute;left:100px;top:80px;color:var(--green);font-weight:700;font-size:22px;line-height:28px;text-transform:uppercase}
.socials{position:absolute;left:137px;top:172px;display:flex;gap:9px}
.socials i{display:block;width:34px;height:34px;border:1.5px solid #ddd;border-radius:50%}
.foot-col{position:absolute;top:76px;font-size:13px;line-height:20px}
.foot-col h5{font-size:17px;font-weight:500;color:#fff;margin-bottom:14px;text-transform:uppercase}
.foot-col li{list-style:none;margin-bottom:13px}
.news-input{position:absolute;left:803px;top:170px;width:297px;height:36px;border:1px solid #777;background:#fff;color:#333;font-size:13px;padding:8px 12px}
.news-send{position:absolute;left:1061px;top:170px;width:39px;height:36px;background:var(--green);display:flex;align-items:center;justify-content:center}
.foot-rule{position:absolute;left:100px;top:290px;width:1000px;height:1px;background:#555}
.copy{position:absolute;top:310px;left:0;width:1200px;text-align:center;font-size:12.5px;color:#ddd}
</style>
</head>
<body>

<header class="site-header">
  <div class="brand">Brookhollow<br>Paint Contractors, LLC</div>
  <div class="contact-bar">
    <span><span class="ico-circle"><svg width="14" height="14" viewBox="0 0 24 24"><path fill="#00AB8E" d="M6.6 10.8a15.2 15.2 0 0 0 6.6 6.6l2.2-2.2c.3-.3.7-.4 1-.2 1.1.4 2.3.6 3.6.6.6 0 1 .4 1 1V20c0 .6-.4 1-1 1C10.6 21 3 13.4 3 4c0-.6.4-1 1-1h3.5c.6 0 1 .4 1 1 0 1.3.2 2.5.6 3.6.1.3 0 .7-.2 1z"/></svg></span>+1 555-214-7390</span>
    <span><span class="ico-circle"><svg width="15" height="12" viewBox="0 0 24 18"><rect x="1" y="1" width="22" height="16" rx="1" fill="none" stroke="#00AB8E" stroke-width="2"/><path d="M1 2l11 8 11-8" fill="none" stroke="#00AB8E" stroke-width="2"/></svg></span>info@BrookhollowPaintContractors.com</span>
  </div>
  <nav class="main-nav">
    <a>HOME</a><i>|</i><a>ABOUT US</a><i>|</i><a>SERVICES</a><i>|</i><a>GALLEY</a><i>|</i><a>CONTACT US</a>
  </nav>
</header>

<section class="hero">
  <svg class="photo" style="left:0;top:0" width="1200" height="630" role="img" aria-label="Smiling painter in red cap and blue overalls rolling white paint onto a wall">
    <defs><linearGradient id="heroG" x1="0" x2="1" y1="0" y2="1"><stop offset="0" stop-color="#f4f4f4"/><stop offset=".55" stop-color="#e6e6e6"/><stop offset="1" stop-color="#c9ced6"/></linearGradient></defs>
    <rect width="1200" height="630" fill="url(#heroG)"/>
  </svg>
  <svg class="arrow" style="left:64px;top:300px" viewBox="0 0 24 40"><path d="M20 2L4 20l16 18" fill="none" stroke="#fff" stroke-width="2"/></svg>
  <svg class="arrow" style="left:1112px;top:300px" viewBox="0 0 24 40"><path d="M4 2l16 18L4 38" fill="none" stroke="#fff" stroke-width="2"/></svg>
  <h1>Brookhollow Paint<br>Contractors, LLC</h1>
  <p>Lorem ipsum dolor sit amet, consectetur adipiscing elit, sed do eiusmod tempor incididunt ut labore et dolore</p>
  <div class="btn" style="left:100px;top:390px;width:155px;height:41px">Get Started</div>
  <svg class="abs" style="left:562px;top:580px" width="84" height="10"><circle cx="5" cy="5" r="4" fill="#bbb"/><circle cx="30" cy="5" r="4" fill="#fff"/><circle cx="55" cy="5" r="4" fill="#bbb"/><circle cx="80" cy="5" r="4" fill="#bbb"/></svg>
</section>

<section class="about">
  <div class="about-frame"></div>
  <svg class="photo" style="left:107px;top:82px" width="469" height="395" role="img" aria-label="Smiling painter in a cap holding a paint roller and a stepladder">
    <defs><linearGradient id="aboutG" x1="0" x2="1"><stop offset="0" stop-color="#eceef0"/><stop offset="1" stop-color="#d4d8dc"/></linearGradient></defs>
    <rect width="469" height="395" fill="url(#aboutG)"/>
  </svg>
  <h2>ABOUT US</h2>
  <div class="abs" style="left:651px;top:154px;width:70px;height:3px;background:var(--green)"></div>
  <p>Lorem ipsum dolor sit amet, consectetur adipiscing elit, sed do eiusmod tempor incididolore magna aliqua. Quis ipsum suspensse ultrices grada. odo viverra maecenas accumsan lacus vel facilisis. Lorum olor sit amet, consecttur adipiscing elit, sed do eiusmod tempor unt ut labore et dolore magna aliqua. Quis ipsum suspse ultrices gravida. Risus commodo viverra maecenas asan lacus vel facilisis.</p>
  <div class="btn" style="left:651px;top:417px;width:155px;height:41px">Learn More</div>
</section>

<section class="services">
  <div class="title">Our Services</div>
  <div class="rule" style="top:130px;background:#fff"></div>

  <div class="card" style="left:100px">
    <svg class="photo" width="320" height="225" role="img" aria-label="Painter on a ladder painting the front of a house"><defs><linearGradient id="s1" x1="0" y1="0" x2="0" y2="1"><stop offset="0" stop-color="#9fc6ea"/><stop offset="1" stop-color="#cfc6bb"/></linearGradient></defs><rect width="320" height="225" fill="url(#s1)"/></svg>
    <div class="badge"><svg width="40" height="40" viewBox="0 0 40 40" fill="none" stroke="#00AB8E" stroke-width="2"><path d="M4 20L20 6l16 14"/><path d="M9 16v19h22V16"/><rect x="16" y="24" width="8" height="11"/></svg></div>
    <h3>RESIDENTIAL PAINTING</h3>
    <p>Lorem ipsum dolor sit amet, sectetur adipiscing elit, ed do eiusmod</p>
    <a>LEARN MORE</a>
  </div>
  <div class="card" style="left:440px">
    <svg class="photo" width="320" height="225" role="img" aria-label="Workers on a red lift painting a modern white building"><defs><linearGradient id="s2" x1="0" y1="0" x2="1" y2="1"><stop offset="0" stop-color="#e9e6df"/><stop offset="1" stop-color="#c9b48a"/></linearGradient></defs><rect width="320" height="225" fill="url(#s2)"/></svg>
    <div class="badge"><svg width="40" height="40" viewBox="0 0 40 40" fill="none" stroke="#00AB8E" stroke-width="2"><rect x="6" y="12" width="12" height="23"/><rect x="18" y="5" width="16" height="30"/><path d="M22 10h3M28 10h3M22 16h3M28 16h3M22 22h3M28 22h3M9 17h3M9 23h3"/></svg></div>
    <h3>COMMERCIAL PAINTING</h3>
    <p>Lorem ipsum dolor sit amet, sectetur adipiscing elit, ed do eiusmod</p>
    <a>LEARN MORE</a>
  </div>
  <div class="card" style="left:781px">
    <svg class="photo" width="320" height="225" role="img" aria-label="Worker spray painting blue metal roof panels"><defs><linearGradient id="s3" x1="0" y1="0" x2="0" y2="1"><stop offset="0" stop-color="#8a8f96"/><stop offset=".5" stop-color="#2f6fd6"/><stop offset="1" stop-color="#9a9a96"/></linearGradient></defs><rect width="320" height="225" fill="url(#s3)"/></svg>
    <div class="badge"><svg width="40" height="40" viewBox="0 0 40 40" fill="none" stroke="#00AB8E" stroke-width="2"><path d="M4 35V18l9 6v-6l9 6v-6l9 6V6h5v29z"/><rect x="9" y="28" width="4" height="4"/><rect x="18" y="28" width="4" height="4"/></svg></div>
    <h3>INDUSTRIAL PAINTING</h3>
    <p>Lorem ipsum dolor sit amet, sectetur adipiscing elit, ed do eiusmod</p>
    <a>LEARN MORE</a>
  </div>
</section>

<section class="gallery">
  <div class="title">Project Gallery</div>
  <div class="rule" style="top:153px;background:var(--green)"></div>
  <svg class="photo" style="left:103px;top:182px" width="644" height="346" role="img" aria-label="Painters working in a bright open-plan office with skylights"><defs><linearGradient id="g1" x1="0" y1="0" x2="1" y2="1"><stop offset="0" stop-color="#c8cdd2"/><stop offset="1" stop-color="#eef0f2"/></linearGradient></defs><rect width="644" height="346" fill="url(#g1)"/></svg>
  <svg class="photo" style="left:755px;top:182px" width="344" height="346" role="img" aria-label="Two-storey stone house with autumn trees"><defs><linearGradient id="g2" x1="0" y1="0" x2="0" y2="1"><stop offset="0" stop-color="#c9a35e"/><stop offset="1" stop-color="#8a7f70"/></linearGradient></defs><rect width="344" height="346" fill="url(#g2)"/></svg>
  <svg class="photo" style="left:103px;top:538px" width="294" height="280" role="img" aria-label="Blue house with a red front door and garden"><defs><linearGradient id="g3" x1="0" y1="0" x2="0" y2="1"><stop offset="0" stop-color="#4d6f9e"/><stop offset="1" stop-color="#5c8a3c"/></linearGradient></defs><rect width="294" height="280" fill="url(#g3)"/></svg>
  <svg class="photo" style="left:407px;top:538px" width="424" height="280" role="img" aria-label="Freshly painted blue-grey office corridor with glass partitions"><defs><linearGradient id="g4" x1="0" y1="0" x2="1" y2="0"><stop offset="0" stop-color="#6e8299"/><stop offset="1" stop-color="#a3afbd"/></linearGradient></defs><rect width="424" height="280" fill="url(#g4)"/></svg>
  <svg class="photo" style="left:843px;top:538px" width="256" height="280" role="img" aria-label="Painters on scaffolding at a new two-storey house"><defs><linearGradient id="g5" x1="0" y1="0" x2="0" y2="1"><stop offset="0" stop-color="#a8c8e8"/><stop offset="1" stop-color="#d9c3a8"/></linearGradient></defs><rect width="256" height="280" fill="url(#g5)"/></svg>
  <div class="btn" style="left:523px;top:844px;width:155px;height:42px">View All</div>
</section>

<section class="reviews">
  <div class="title">What Customers Say</div>
  <div class="rule" style="top:128px;background:var(--red)"></div>
  <svg class="arrow" style="left:62px;top:298px" viewBox="0 0 24 40"><path d="M20 2L4 20l16 18" fill="none" stroke="#333" stroke-width="2"/></svg>
  <svg class="arrow" style="left:1116px;top:298px" viewBox="0 0 24 40"><path d="M4 2l16 18L4 38" fill="none" stroke="#333" stroke-width="2"/></svg>

  <div class="quote" style="left:103px">
    <div class="avatar" role="img" aria-label="Customer portrait"></div>
    <p>Lorem ipsum dolor sit amet, consectetur adipiscing elit, sed do eiusmod tempor incididunt ut labore et dolore magna aliqua. Quis ium suspendisse ultrices gravida. Risus commodo viverra</p>
    <div class="mark">”</div>
  </div>
  <div class="who" style="left:103px">Daniel Reyes</div>
  <div class="stars" style="left:103px">★★★★★</div>

  <div class="quote" style="left:618px">
    <div class="avatar" role="img" aria-label="Customer portrait"></div>
    <p>Lorem ipsum dolor sit amet, consectetur adipiscing elit, sed do eiusmod tempor incididunt ut labore et dolore magna aliqua. Quis ium suspendisse ultrices gravida. Risus commodo viverra</p>
    <div class="mark">”</div>
  </div>
  <div class="who" style="left:618px">Daniel Reyes</div>
  <div class="stars" style="left:618px">★★★★★</div>

  <div class="dots"><i></i><i class="on"></i><i></i></div>
</section>

<section class="blog">
  <div class="title">Latest Blog</div>
  <div class="rule" style="top:140px;background:var(--green)"></div>

  <div class="post" style="left:100px">
    <svg class="photo" width="314" height="190" role="img" aria-label="Two painters on ladders painting an exterior wall"><defs><linearGradient id="b1" x1="0" y1="0" x2="1" y2="0"><stop offset="0" stop-color="#9cc4e6"/><stop offset="1" stop-color="#e8e8e8"/></linearGradient></defs><rect width="314" height="190" fill="url(#b1)"/></svg>
    <div class="date"><span>JAN</span><span>2023</span></div>
    <div class="box">
      <div class="meta"><span>◌ 2 Comments</span><span>♙ By Admin</span></div>
      <h4>The standard Lorem Ipssag<br>used since the 1500s</h4>
      <p>Lorem ipsum dolor sit at, consectdetur adipiscing elit, sed do eiusmod tempor incididunt ut labore et dolore</p>
    </div>
  </div>
  <div class="post" style="left:443px">
    <svg class="photo" width="314" height="190" role="img" aria-label="Painter and client reviewing plans in a white room"><defs><linearGradient id="b2" x1="0" y1="0" x2="1" y2="0"><stop offset="0" stop-color="#eeeeee"/><stop offset="1" stop-color="#d6d2c8"/></linearGradient></defs><rect width="314" height="190" fill="url(#b2)"/></svg>
    <div class="date"><span>JAN</span><span>2023</span></div>
    <div class="box">
      <div class="meta"><span>◌ 2 Comments</span><span>♙ By Admin</span></div>
      <h4>The standard Lorem Ipssag<br>used since the 1500s</h4>
      <p>Lorem ipsum dolor sit at, consectdetur adipiscing elit, sed do eiusmod tempor incididunt ut labore et dolore</p>
    </div>
  </div>
  <div class="post" style="left:787px">
    <svg class="photo" width="314" height="190" role="img" aria-label="Painter in a hard hat rolling yellow paint on a wall"><defs><linearGradient id="b3" x1="0" y1="0" x2="1" y2="0"><stop offset="0" stop-color="#f2d22e"/><stop offset="1" stop-color="#e9e4c8"/></linearGradient></defs><rect width="314" height="190" fill="url(#b3)"/></svg>
    <div class="date"><span>JAN</span><span>2023</span></div>
    <div class="box">
      <div class="meta"><span>◌ 2 Comments</span><span>♙ By Admin</span></div>
      <h4>The standard Lorem Ipssag<br>used since the 1500s</h4>
      <p>Lorem ipsum dolor sit at, consectdetur adipiscing elit, sed do eiusmod tempor incididunt ut labore et dolore</p>
    </div>
  </div>
</section>

<section class="get-in-touch">
  <svg class="photo" style="left:0;top:0" width="1200" height="565" role="img" aria-label="Painter on a stepladder rolling turquoise paint onto a room wall">
    <defs><linearGradient id="ct" x1="0" x2="1"><stop offset="0" stop-color="#4fc3d2"/><stop offset=".45" stop-color="#7fd3dc"/><stop offset=".62" stop-color="#eef3f4"/><stop offset="1" stop-color="#f3f3f3"/></linearGradient></defs>
    <rect width="1200" height="565" fill="url(#ct)"/>
  </svg>
  <h2>Get In Touch</h2>
  <div class="field" style="top:144px">First Name</div>
  <div class="field" style="top:194px">Last Name</div>
  <div class="field" style="top:244px">Email</div>
  <div class="field" style="top:294px">Phone Number</div>
  <div class="field msg" style="top:344px">Message</div>
  <div class="btn" style="left:662px;top:448px;width:139px;height:36px">Submit</div>
</section>

<footer class="site-footer">
  <div class="foot-brand">Brookhollow<br>Paint Contractors, LLC</div>
  <div class="socials"><i></i><i></i><i></i><i></i></div>

  <div class="foot-col" style="left:403px">
    <h5>Contact Us</h5>
    <ul>
      <li>📍 482 Alder Ridge Rd<br>&nbsp;&nbsp;&nbsp;Fairmont, US 40213</li>
      <li>✆ +1 555-214-7390</li>
      <li>✉ info@BrookhollowPaint<br>&nbsp;&nbsp;&nbsp;Contractors.com</li>
    </ul>
  </div>
  <div class="foot-col" style="left:632px">
    <h5>Quick Links</h5>
    <ul><li>Home</li><li>About Us</li><li>Services</li><li>Gallery</li><li>Contact Us</li></ul>
  </div>
  <div class="foot-col" style="left:803px;width:300px">
    <h5>Sign For Newslatter</h5>
    <p>Stay connected on new products, events and offers. Valid for new email subscribers only.</p>
  </div>
  <div class="news-input">Eamil</div>
  <div class="news-send"><svg width="16" height="16" viewBox="0 0 24 24"><path fill="#fff" d="M2 11L22 2l-9 20-2-8z"/></svg></div>

  <div class="foot-rule"></div>
  <div class="copy">Copyright ©2023 BROOKHOLLOW PAINT CONTRACTORS, LLC. All Rights Reserved.</div>
</footer>

</body>
</html>
```